Business Card Design Project

We need a business card design for an existing company in Dallas/Fort Worth that is expanding services and re-branding. We are changing the name from Bristow Commercial Cleaning to Kelmont Facility Services. We are expanding from only commercial cleaning to include complete commercial landscape and facility maintenance services, too.

As stated, we offer a package of services that includes landscape, janitorial and facility services, which is largely unique in the industry.

We would like a design that communicates trust/partnership with a professional, corporate image, but not necessarily using the standard white business card. We would like a design that perhaps uses darker blues or perhaps a gray background, but we are open to other ideas. We might also be interested in a double-sided design - maybe with our logo on the back, printed on a gray background?

We will probably stick with the attached logo, but if you've got another inspired idea....

Target Market(s)

Property managers, commercial real estate professionals, corporate executives

Industry/Entity Type

Landscape

Requirements
Should not have
• Not interested in old style fonts.

```html
<!DOCTYPE html>
<html lang="en">
<head>
<meta charset="utf-8">
<title>Kelmont Facility Services – Business Card</title>
<link href="https://fonts.googleapis.com/css2?family=Lato:wght@400;700&display=swap" rel="stylesheet">
<style>
  :root {
    --navy: #0b4a7e;
    --navy-deep: #083b66;
    --ink: #2e2e2e;
    --ink-soft: #444444;
    --paper: #ffffff;
    --stage: #dfe4e8;
  }
  * { box-sizing: border-box; margin: 0; padding: 0; }
  html, body {
    width: 1200px; height: 960px; overflow: hidden;
    background: var(--stage);
    font-family: "Lato", sans-serif;
  }
  .sheet {
    width: 1200px; height: 960px;
    display: flex; flex-direction: column;
    align-items: center; justify-content: center; gap: 56px;
  }
  .card {
    position: relative;
    width: 700px; height: 400px;
    box-shadow: 0 6px 18px rgba(0,0,0,0.18);
    overflow: hidden;
  }

  /* Front */
  .card--front { background: var(--paper); color: var(--ink); }
  .holder { position: absolute; left: 48px; top: 70px; }
  .holder__name { font-size: 31px; font-weight: 400; letter-spacing: 0.5px; text-transform: uppercase; line-height: 1.2; }
  .holder__role { font-size: 18px; margin-top: 6px; color: var(--ink-soft); }
  .contact { position: absolute; left: 48px; top: 180px; list-style: none; }
  .contact__item { display: flex; align-items: center; gap: 16px; font-size: 20px; line-height: 30px; }
  .contact__icon { width: 18px; height: 18px; fill: var(--navy); }
  .address { position: absolute; left: 48px; top: 256px; font-size: 19px; line-height: 30px; font-style: normal; }
  .web-band {
    position: absolute; left: 0; bottom: 30px;
    width: 430px; height: 40px; background: var(--navy);
    color: var(--paper); font-size: 18px;
    display: flex; align-items: center; padding-left: 48px;
  }
  .brand-name {
    position: absolute; right: 48px; top: 76px;
    color: var(--ink); font-size: 22px; font-weight: 700; letter-spacing: 1px;
  }

  /* Back */
  .card--back {
    background: linear-gradient(135deg, var(--navy) 0%, var(--navy-deep) 100%);
    color: var(--paper);
  }
  .lockup {
    position: absolute; right: 30px; bottom: 56px;
    text-align: left;
  }
  .lockup__name { font-size: 30px; font-weight: 400; letter-spacing: 3px; text-transform: uppercase; line-height: 1.1; }
  .lockup__tagline { font-size: 13px; letter-spacing: 0.6px; margin-top: 6px; }
  .edge-rule { position: absolute; right: 12px; bottom: 56px; width: 3px; height: 70px; background: var(--paper); }
</style>
</head>
<body>
<main class="sheet">

  <section class="card card--front" aria-label="Card front">
    <div class="holder">
      <h1 class="holder__name">Marissa Holloway</h1>
      <p class="holder__role">Director</p>
    </div>

    <ul class="contact">
      <li class="contact__item">
        <svg class="contact__icon" viewBox="0 0 24 24" aria-label="Phone"><path d="M6.6 10.8a15.1 15.1 0 0 0 6.6 6.6l2.2-2.2a1 1 0 0 1 1-.25 11.4 11.4 0 0 0 3.6.57 1 1 0 0 1 1 1V20a1 1 0 0 1-1 1A17 17 0 0 1 3 4a1 1 0 0 1 1-1h3.5a1 1 0 0 1 1 1c0 1.25.2 2.45.57 3.57a1 1 0 0 1-.25 1z"/></svg>
        <span>214-555-0187</span>
      </li>
      <li class="contact__item">
        <svg class="contact__icon" viewBox="0 0 24 24" aria-label="Fax"><path d="M6 2h12v5H6zM3 8h18a1 1 0 0 1 1 1v8h-4v5H6v-5H2V9a1 1 0 0 1 1-1zm5 7v5h8v-5z"/></svg>
        <span>214-555-0187</span>
      </li>
    </ul>

    <address class="address">
      Level 2, 48 Carrow Street<br>
      PO Box 2210, Dallas 75201
    </address>

    <div class="web-band">www.kelmontfacilityservices.com</div>

    <p class="brand-name">KELMONT</p>
  </section>

  <section class="card card--back" aria-label="Card back">
    <div class="lockup">
      <p class="lockup__name">Kelmont Facility Services</p>
      <p class="lockup__tagline">Grounds, Cleaning and Building Care Under One Contract</p>
    </div>
    <span class="edge-rule"></span>
  </section>

</main>
</body>
</html>
```